U.S. Popcorn company needs business cards

We are a popcorn company that manufactures popcorn and sells it to grocery stores worldwide. Our theme is "Americana" and our logo is Kettle Mesa Byway which is the most famous highway in the U.S.

We would like the design to be simple and to use both sides. On the back side we would like to see just the logo and website. The front would be normal details

Target Market(s)

Wholesalers, grocers and distributors

Industry/Entity Type

Manufacture

Contact Information for Business Card

Business name: Kettle Mesa Popcorn
Phone: +1 555 014 2286
Email: Dale@kettlemesapopcorn.com
website: www.kettlemesapopcorn.com
Tag Line: "Freshly popped daily"
Name: Dale Whitcombe
Title: Founder/President

Requirements
Must have
• Either this design should be fun or clean and simple. I will let you show me your thougths.
Nice to have
• Anything that ties in the real Kettle Mesa Byway.
• Colors might need to be red, white and blue incorporated.
Should not have
• Not be too busy.

```html
<!DOCTYPE html>
<html lang="en">
<head>
<meta charset="utf-8">
<title>Kettle Mesa Popcorn — Business Cards</title>
<link href="https://fonts.googleapis.com/css2?family=Lato:wght@400;700&display=swap" rel="stylesheet">
<style>
  :root {
    --navy: #2a3a96;
    --navy-deep: #1e2a78;
    --navy-light: #3447a8;
    --red: #e2262f;
    --white: #ffffff;
    --paper: #f3f3f3;
    --stage: #e9e6e1;
  }
  * { box-sizing: border-box; margin: 0; padding: 0; }
  html, body {
    width: 1200px; height: 780px; overflow: hidden;
    background: var(--stage);
    font-family: "Lato", Arial, sans-serif;
  }
  .sheet {
    width: 1200px; height: 780px;
    display: flex; align-items: center; justify-content: center; gap: 60px;
  }
  .card {
    position: relative;
    width: 520px; height: 300px;
    border-radius: 4px; overflow: hidden;
    box-shadow: 0 8px 22px rgba(0,0,0,.22);
  }
  .card-front { background: var(--paper); }
  .front-bg { position: absolute; inset: 0; }
  .brand-mark {
    position: absolute; left: 30px; top: 100px; width: 190px;
    display: flex; flex-direction: column; align-items: center; gap: 10px;
    text-align: center;
  }
  .brand-dot { width: 34px; height: 34px; border-radius: 50%; background: var(--red); }
  .brand-name { color: var(--navy); font-weight: 700; font-size: 22px; line-height: 1.15; }
  .details {
    position: absolute; left: 300px; top: 24px; width: 205px;
    color: var(--white); text-align: left;
  }
  .company { font-size: 20px; font-weight: 700; line-height: 1.1; }
  .tagline { font-size: 12px; margin-top: 3px; }
  .person { margin-top: 16px; }
  .person-name { font-size: 17px; }
  .person-title { font-size: 12px; color: var(--red); margin-top: 2px; }
  .location { margin-top: 14px; font-size: 12px; line-height: 1.35; }
  .contacts { margin-top: 12px; list-style: none; font-size: 11.5px; line-height: 1.7; }
  .contacts li { display: flex; align-items: center; gap: 6px; white-space: nowrap; }
  .contacts svg { width: 11px; height: 11px; flex: none; }

  .card-back {
    background: radial-gradient(ellipse at 50% 45%, var(--navy-light), var(--navy-deep) 80%);
    display: flex; flex-direction: column; align-items: center; justify-content: center; gap: 26px;
  }
  .back-mark { display: flex; align-items: center; gap: 12px; }
  .back-mark .brand-name { color: var(--white); font-size: 30px; }
  .back-mark .brand-dot { width: 40px; height: 40px; }
  .back-url { color: var(--white); font-size: 14px; letter-spacing: .3px; }
  .back-url .url-domain { color: var(--red); }
</style>
</head>
<body>
<main class="sheet">
  <section class="card card-front" aria-label="Card front">
    <svg class="front-bg" viewBox="0 0 520 300" preserveAspectRatio="none" aria-hidden="true">
      <defs>
        <linearGradient id="navyFade" x1="0" y1="0" x2="1" y2="1">
          <stop offset="0" stop-color="#3447a8"/>
          <stop offset="1" stop-color="#1e2a78"/>
        </linearGradient>
      </defs>
      <path d="M210,0 C250,95 240,215 282,300 L520,300 L520,0 Z" fill="#e2262f"/>
      <path d="M220,0 C260,95 250,215 292,300 L520,300 L520,0 Z" fill="#ffffff"/>
      <path d="M226,0 C266,95 256,215 298,300 L520,300 L520,0 Z" fill="url(#navyFade)"/>
    </svg>
    <div class="brand-mark">
      <span class="brand-dot"></span>
      <span class="brand-name">Kettle Mesa Popcorn</span>
    </div>
    <div class="details">
      <h1 class="company">Kettle Mesa Popcorn</h1>
      <p class="tagline">Freshly popped daily</p>
      <div class="person">
        <p class="person-name">Dale Whitcombe</p>
        <p class="person-title">Founder/President</p>
      </div>
      <p class="location">Mesa Hollow, CA<br>United States</p>
      <ul class="contacts">
        <li><svg viewBox="0 0 12 12"><rect width="12" height="12" rx="2" fill="#e2262f"/><path d="M3.2 2.5l1.5 0 .6 1.8-.9.7c.4.9 1 1.5 1.9 1.9l.7-.9 1.8.6v1.5c-3.4.2-5.8-2.2-5.6-5.6z" fill="#fff"/></svg>+1 555 014 2286</li>
        <li><svg viewBox="0 0 12 12"><rect width="12" height="12" rx="2" fill="#e2262f"/><path d="M2.5 3.8h7v4.6h-7z M2.5 3.8l3.5 2.6 3.5-2.6" fill="none" stroke="#fff" stroke-width=".9"/></svg>Dale@kettlemesapopcorn.com</li>
        <li><svg viewBox="0 0 12 12"><circle cx="6" cy="6" r="6" fill="#e2262f"/><circle cx="6" cy="6" r="3.4" fill="none" stroke="#fff" stroke-width=".8"/><path d="M2.6 6h6.8M6 2.6c-1.6 2-1.6 4.8 0 6.8M6 2.6c1.6 2 1.6 4.8 0 6.8" fill="none" stroke="#fff" stroke-width=".7"/></svg>www.kettlemesapopcorn.com</li>
      </ul>
    </div>
  </section>

  <section class="card card-back" aria-label="Card back">
    <div class="back-mark">
      <span class="brand-dot"></span>
      <span class="brand-name">Kettle Mesa Popcorn</span>
    </div>
    <p class="back-url">www.<span class="url-domain">kettlemesapopcorn</span>.com</p>
  </section>
</main>
</body>
</html>
```